New Podcast, Ridgewater Wellness Bureaus

We need a cover design for a new podcast that we are producing.

Title: Ridgewater Wellness Bureaus

This is a business podcast for Native American tribal organizations, representing indigenous peoples of the United States.

Pull colors from the logo.
Do not add photos of people into the design.

Public Health, Statistics, Epidemiology, Tribal Organizations, NonProfits

```html
<!DOCTYPE html>
<html lang="en">
<head>
<meta charset="utf-8">
<title>Ridgewater Wellness Bureaus – Podcast Cover</title>
<link rel="stylesheet" href="https://fonts.googleapis.com/css2?family=Bebas+Neue&family=Oswald:wght@500;600&family=Mr+Dafoe&display=swap">
<style>
  :root {
    --navy: #0b2663;
    --royal: #1552b0;
    --sky: #2f7fe0;
    --white: #ffffff;
    --teal: #0f7f7c;
    --orange: #c8722f;
    --red: #c8102e;
    --crimson: #8c0f2e;
    --pink: #e0245e;
  }
  html, body {
    margin: 0;
    padding: 0;
    width: 1200px;
    height: 1200px;
    overflow: hidden;
  }
  .cover {
    position: relative;
    width: 1200px;
    height: 1200px;
    overflow: hidden;
    background: radial-gradient(circle at 75% 35%, var(--royal) 0%, #0e3b8c 45%, var(--navy) 100%);
    font-family: "Bebas Neue", "Oswald", sans-serif;
    color: var(--white);
  }
  .flag-bands {
    position: absolute;
    inset: 0;
  }
  .brand-tab {
    position: absolute;
    top: 0;
    left: 780px;
    width: 376px;
    height: 182px;
    background: var(--white);
    border-radius: 0 0 0 28px;
    display: flex;
    align-items: center;
    gap: 18px;
    padding-left: 28px;
    box-sizing: border-box;
  }
  .brand-mark {
    width: 92px;
    height: 92px;
    border-radius: 50%;
    background: var(--orange);
    flex: none;
  }
  .brand-name {
    font-family: "Oswald", sans-serif;
    font-weight: 600;
    font-size: 25px;
    line-height: 1.05;
    color: var(--teal);
    text-transform: uppercase;
    text-align: center;
    letter-spacing: 0.5px;
  }
  .headline {
    position: absolute;
    left: 100px;
    top: 118px;
    margin: 0;
    font-weight: 400;
    text-shadow: 6px 8px 14px rgba(0, 0, 20, 0.45);
  }
  .headline span { display: block; }
  .headline .lead {
    font-size: 96px;
    line-height: 1;
    letter-spacing: -1px;
  }
  .headline .accent {
    font-size: 222px;
    line-height: 0.86;
    margin-top: 6px;
    background: linear-gradient(90deg, var(--teal), var(--orange) 45%, var(--red) 70%, var(--teal));
    -webkit-background-clip: text;
    background-clip: text;
    color: transparent;
    text-shadow: none;
    filter: drop-shadow(6px 8px 10px rgba(0, 0, 20, 0.45));
  }
  .headline .line {
    font-size: 262px;
    line-height: 0.84;
  }
  .credits {
    position: absolute;
    left: 118px;
    top: 905px;
    display: flex;
    align-items: center;
    gap: 34px;
  }
  .host .script, .format .script {
    font-family: "Mr Dafoe", cursive;
    font-size: 48px;
    line-height: 0.8;
    display: block;
  }
  .host .name {
    font-family: "Oswald", sans-serif;
    font-weight: 500;
    font-style: italic;
    font-size: 72px;
    line-height: 1;
    letter-spacing: -3px;
    display: block;
  }
  .divider {
    width: 2px;
    height: 120px;
    background: rgba(255, 255, 255, 0.7);
  }
  .format {
    position: relative;
    font-family: "Oswald", sans-serif;
    font-weight: 500;
    font-style: italic;
    letter-spacing: -3px;
  }
  .format .live { font-size: 62px; line-height: 1; display: block; }
  .format .script { position: absolute; left: 78px; top: 22px; letter-spacing: 0; }
  .format .kind { font-size: 72px; line-height: 0.9; display: block; margin-left: -14px; }
  .actions {
    position: absolute;
    left: 120px;
    top: 1073px;
    display: flex;
    align-items: center;
    gap: 38px;
  }
  .listen-btn {
    background: var(--orange);
    border-radius: 10px;
    width: 195px;
    height: 59px;
    display: flex;
    align-items: center;
    justify-content: center;
    font-size: 50px;
    line-height: 1;
    padding-top: 4px;
    box-sizing: border-box;
  }
  .social { display: flex; gap: 8px; }
  .social span {
    width: 38px;
    height: 38px;
    border-radius: 50%;
    background: var(--white);
  }
</style>
</head>
<body>
<div class="cover">
  <svg class="flag-bands" viewBox="0 0 1200 1200" aria-hidden="true">
    <polygon points="1020,610 1200,470 1200,520 1060,610" fill="#0a1a3a" opacity="0.7"/>
    <polygon points="1040,660 1200,540 1200,610 1090,660" fill="var(--crimson)" opacity="0.85"/>
    <polygon points="1080,720 1200,630 1200,700 1130,720" fill="#0a1a3a" opacity="0.6"/>
    <polygon points="1140,760 1200,720 1200,760" fill="var(--white)"/>
    <polygon points="770,1050 1200,760 1200,900 990,1050" fill="var(--pink)" opacity="0.85"/>
    <polygon points="840,1200 1200,930 1200,1010 950,1200" fill="var(--red)"/>
    <polygon points="690,1200 1110,1060 1030,1200" fill="var(--white)" opacity="0.9"/>
    <polygon points="600,1200 1060,1050 1090,1050 660,1200" fill="var(--crimson)"/>
    <polygon points="480,1200 900,1000 930,1000 560,1200" fill="var(--sky)" opacity="0.55"/>
    <polygon points="990,1200 1200,1050 1200,1200" fill="var(--sky)" opacity="0.8"/>
    <polygon points="1030,1200 1200,1080 1200,1100 1060,1200" fill="var(--white)"/>
  </svg>

  <div class="brand-tab">
    <span class="brand-mark"></span>
    <span class="brand-name">Ridgewater<br>Wellness<br>Bureaus</span>
  </div>

  <h1 class="headline">
    <span class="lead">Discussion about</span>
    <span class="accent" role="img" aria-label="Ridgewater, lettered with a woven geometric tribal pattern in teal, orange and red">RIDGEWATER</span>
    <span class="line">WELLNESS</span>
    <span class="line">BUREAUS</span>
  </h1>

  <div class="credits">
    <div class="host">
      <span class="script">Hosted By</span>
      <span class="name">Mr.Calder</span>
    </div>
    <div class="divider"></div>
    <div class="format">
      <span class="live">Live</span>
      <span class="script">Stream</span>
      <span class="kind">podcast</span>
    </div>
  </div>

  <div class="actions">
    <div class="listen-btn">LISTEN NOW</div>
    <div class="social" aria-label="Social channels">
      <span></span><span></span><span></span><span></span>
    </div>
  </div>
</div>
</body>
</html>
```